" A MOURALVES E TEIXEDO SOCIEDADE DE ADVOGADOS é a concretização de um ideal instituído nos idos de 2007, tempo em que os sócios fundadores ainda ocupavam os bancos da Faculdade de Direito. Sediada no Jardim Vila Aurora na cidade de Itaverde, seu Escritório conta com modernas instalações e com uma equipe selecionada de Advogados e Colaboradores especializados. Atualmente, em decorrência de sua organização operacional e do comprometimento ético e intelectual de seus profissionais, a Sociedade vem conquistando padrões de excelência e qualidade na prestação de serviços jurídicos, se sustentando em posição de destaque no cenário na Advocacia de Itaverde e Região. "

```html
<!DOCTYPE html>
<html lang="pt-BR">
<head>
<meta charset="UTF-8">
<title>Assinatura de Email – Mouralves e Teixedo</title>
<link href="https://fonts.googleapis.com/css2?family=Open+Sans:wght@400;600;700&display=swap" rel="stylesheet">
<style>
  :root {
    --navy: #0f2a47;
    --navy-deep: #0a1f36;
    --gold: #c9a45a;
    --gold-light: #e6cf95;
    --gold-dark: #9c7a3a;
    --paper: #ffffff;
    --ink: #1b2f4a;
    --bg: #ececec;
    --bg-edge: #dcdcdc;
  }
  * { box-sizing: border-box; margin: 0; padding: 0; }
  html, body { width: 1200px; height: 1200px; overflow: hidden; }
  body {
    position: relative;
    font-family: "Open Sans", Arial, sans-serif;
    background: radial-gradient(circle at 50% 45%, #f7f7f7 0%, var(--bg) 55%, var(--bg-edge) 100%);
  }

  .section-label {
    position: absolute; left: 84px; top: 29px;
    width: 340px; height: 44px;
    background: var(--navy);
    clip-path: polygon(4% 0, 100% 0, 96% 100%, 0 100%);
    color: #fff; font-size: 22px; font-weight: 600;
    display: flex; align-items: center; padding-left: 40px;
    letter-spacing: 0.5px;
  }
  .section-accent {
    position: absolute; left: 400px; top: 22px;
    width: 30px; height: 20px;
    background: var(--gold);
    clip-path: polygon(0 0, 100% 0, 100% 100%);
  }

  .signature { position: absolute; left: 120px; width: 960px; }
  .signature--dark { top: 326px; }
  .signature--light { top: 689px; }

  .name-tab {
    position: absolute; right: 0; top: 0;
    width: 564px; height: 51px;
    background: linear-gradient(90deg, var(--gold-dark), var(--gold) 35%, var(--gold-light) 75%, var(--gold));
    clip-path: polygon(5% 0, 100% 0, 100% 100%, 0 100%);
    color: #fff; font-weight: 700; font-size: 21px;
    display: flex; align-items: center; padding-left: 68px;
  }
  .name-tab .oab { font-weight: 400; }

  .card {
    position: absolute; left: 0; top: 51px;
    width: 960px; height: 261px;
    border-radius: 14px 0 14px 14px;
    overflow: hidden;
  }
  .signature--light .card { height: 250px; }
  .signature--dark .card { background: linear-gradient(120deg, var(--navy) 0%, var(--navy-deep) 100%); }
  .signature--light .card {
    background: linear-gradient(120deg, #ffffff 0%, #f1f1f1 100%);
    box-shadow: 0 4px 14px rgba(0,0,0,0.12);
  }
  .card-edge {
    position: absolute; right: 0; top: 0;
    width: 14px; height: 100%;
    background: linear-gradient(180deg, var(--gold-light), var(--gold) 50%, var(--gold-dark));
  }
  .card-base {
    position: absolute; left: 0; bottom: 0;
    width: 100%; height: 6px;
    background: linear-gradient(90deg, var(--gold-dark), var(--gold-light) 50%, var(--gold));
  }

  .brand {
    position: absolute; left: 0; top: 0;
    width: 520px; height: 100%;
    display: flex; flex-direction: column; align-items: center; justify-content: center;
    text-align: center;
  }
  .brand-mark {
    width: 80px; height: 80px; border-radius: 50%;
    background: linear-gradient(135deg, var(--gold-light), var(--gold-dark));
    margin-bottom: 14px;
  }
  .brand-name {
    font-weight: 700; font-size: 31px; line-height: 1.15;
    color: #fff;
  }
  .brand-name small { display: block; font-size: 15px; letter-spacing: 3px; margin-top: 4px; }
  .signature--light .brand-name { color: var(--ink); }
  .brand-site {
    margin-top: 14px; font-size: 20px; letter-spacing: 0.8px; color: #fff;
  }
  .signature--light .brand-site { color: var(--ink); }

  .contact {
    position: absolute; right: 48px; top: 24px;
    text-align: right; font-size: 20px; line-height: 29px;
    color: #fff;
  }
  .signature--light .contact { color: var(--ink); top: 18px; }
  .contact dt { color: var(--gold); font-weight: 700; }
  .contact dd { margin-bottom: 12px; }
  .contact address { font-style: normal; margin-top: 22px; }
</style>
</head>
<body>
  <div class="section-label">ASSINATURA DE EMAIL</div>
  <div class="section-accent"></div>

  <section class="signature signature--dark">
    <div class="name-tab">Marcos Andrade Teixedo -&nbsp;<span class="oab">OAB/SP 482.516</span></div>
    <div class="card">
      <div class="brand">
        <div class="brand-mark"></div>
        <div class="brand-name">MOURALVES E TEIXEDO<small>SOCIEDADE DE ADVOGADOS</small></div>
        <div class="brand-site">www.mouralvesteixedo.adv.br</div>
      </div>
      <div class="contact">
        <dl>
          <dt>Telefone:</dt><dd>+ 55 (15) 3210 4857</dd>
          <dt>Email:</dt><dd>marcos@mouralvesteixedo.adv.br</dd>
        </dl>
        <address>Rua Professor Elias Mota, 418<br>Vila Aurora | Itaverde | SP | CEP 18095-230</address>
      </div>
      <div class="card-edge"></div>
    </div>
  </section>

  <section class="signature signature--light">
    <div class="name-tab">Marcos Andrade Teixedo -&nbsp;<span class="oab">OAB/SP 482.516</span></div>
    <div class="card">
      <div class="brand">
        <div class="brand-mark"></div>
        <div class="brand-name">MOURALVES E TEIXEDO<small>SOCIEDADE DE ADVOGADOS</small></div>
        <div class="brand-site">www.mouralvesteixedo.adv.br</div>
      </div>
      <div class="contact">
        <dl>
          <dt>Telefone:</dt><dd>+ 55 (15) 3210 4857</dd>
          <dt>Email:</dt><dd>marcos@mouralvesteixedo.adv.br</dd>
        </dl>
        <address>Rua Professor Elias Mota, 418<br>Vila Aurora | Itaverde | SP | CEP 18095-230</address>
      </div>
      <div class="card-edge"></div>
      <div class="card-base"></div>
    </div>
  </section>
</body>
</html>
```